Vantrel Consulting Business card design.

See our website www.vantrelconsulting.com which will give you a good idea of what we are about. The font is called 'Play'.

I'd like a standout business card in keeping with the themes and branding on the website

Target Market(s)

professionals. HR directors

Industry/Entity Type

Business

Contact Information for Business Card

Vantrel Consulting PO Box 3917 Marrowdene NSW 2279 1300 584 316 Gareth Lindqvane Principal email: career@vantrelconsulting.com ABN: 41293087614

Other font styles liked:
• Play

Requirements
Must have
• Must have same design colours and branding as website.
• On back I'd prefer a list of the things we do which appears below the name at the header on the website

```html
<!DOCTYPE html>
<html lang="en">
<head>
<meta charset="utf-8">
<title>Vantrel Consulting – Business Card</title>
<link rel="stylesheet" href="https://fonts.googleapis.com/css2?family=Play:wght@400;700&display=swap">
<style>
  :root {
    --stage: #878787;
    --navy: #0e1e2f;
    --slate: #474747;
    --silver: #8c8c8c;
    --accent: #3a8fd2;
    --white: #ffffff;
    --sky-top: #3a67c0;
    --sky-mid: #2d74cf;
    --snow: #d9e6f7;
  }
  * { box-sizing: border-box; margin: 0; padding: 0; }
  html, body {
    width: 992px; height: 1200px; overflow: hidden;
    background: var(--stage);
    font-family: 'Play', sans-serif;
  }
  .card {
    position: absolute; left: 67px;
    width: 862px; height: 491px;
    overflow: hidden;
    box-shadow: 6px 8px 10px rgba(0,0,0,0.45);
  }
  .card--front { top: 66px; background: var(--slate); }
  .card--back { top: 621px; background: var(--navy); }

  .front-shape { position: absolute; inset: 0; width: 100%; height: 100%; }

  .wordmark {
    position: absolute;
    font-weight: 400; font-size: 52px; line-height: 1;
    color: var(--white); letter-spacing: 0.5px; white-space: nowrap;
  }
  .services {
    position: absolute;
    font-size: 14.5px; letter-spacing: 1.6px;
    color: var(--accent); white-space: nowrap;
  }
  .services .sep { margin: 0 5px; }

  .card--front .wordmark { left: 40px; top: 39px; }
  .card--front .services { left: 40px; top: 112px; }

  .person { position: absolute; left: 40px; top: 181px; }
  .person__name { font-size: 27px; color: var(--accent); line-height: 1.2; }
  .person__role { font-size: 21px; color: var(--white); line-height: 1.4; }

  .contacts { position: absolute; left: 40px; top: 290px; list-style: none; }
  .contacts li {
    display: flex; align-items: center;
    height: 30.5px; font-size: 21px; color: var(--white);
  }
  .contacts svg { width: 18px; height: 18px; margin-right: 18px; flex: none; }

  .abn { position: absolute; left: 38px; top: 416px; font-size: 21px; color: var(--white); }

  .photo-area {
    position: absolute; left: 0; top: 0; width: 100%; height: 343px;
    background: linear-gradient(180deg, var(--sky-top) 0%, var(--sky-mid) 55%, var(--snow) 100%);
  }
  .card--back .wordmark { right: 57px; top: 371px; }
  .card--back .services { right: 50px; top: 443px; }
</style>
</head>
<body>

<section class="card card--front" aria-label="Business card front">
  <svg class="front-shape" viewBox="0 0 862 491" preserveAspectRatio="none" aria-hidden="true">
    <path fill="var(--silver)" d="M826 0 H838 C818 260 700 430 456 491 H210 C596 446 794 250 826 0 Z"/>
    <path fill="var(--navy)" d="M0 0 H826 C794 250 596 446 210 491 H0 Z"/>
  </svg>

  <h1 class="wordmark">VANTREL CONSULTING</h1>
  <p class="services">Search &amp; Select<span class="sep">|</span>Career<span class="sep">|</span>Coaching<span class="sep">|</span>Leadership<span class="sep">|</span>Outplacement</p>

  <div class="person">
    <p class="person__name">Gareth Lindqvane</p>
    <p class="person__role">Principal</p>
  </div>

  <ul class="contacts">
    <li>
      <svg viewBox="0 0 18 18" aria-hidden="true"><rect width="18" height="18" fill="var(--accent)"/><path fill="var(--navy)" d="M5 3.5h2.5l1 3-1.5 1c.7 1.5 1.8 2.6 3.3 3.3l1-1.5 3 1V13c0 .8-.7 1.5-1.5 1.5C7.6 14.5 3.5 10.4 3.5 5 3.5 4.2 4.2 3.5 5 3.5z"/></svg>
      1300 584 316
    </li>
    <li>
      <svg viewBox="0 0 18 18" aria-hidden="true"><rect width="18" height="18" fill="var(--accent)"/><rect x="3.5" y="5" width="11" height="8" fill="none" stroke="var(--navy)" stroke-width="1.4"/><path d="M3.5 5l5.5 4.5L14.5 5" fill="none" stroke="var(--navy)" stroke-width="1.4"/></svg>
      career@vantrelconsulting.com
    </li>
    <li>
      <svg viewBox="0 0 18 18" aria-hidden="true"><rect width="18" height="18" fill="var(--accent)"/><path fill="var(--navy)" d="M9 3a4 4 0 0 1 4 4c0 3-4 8-4 8S5 10 5 7a4 4 0 0 1 4-4zm0 2.5a1.5 1.5 0 1 0 0 3 1.5 1.5 0 0 0 0-3z"/></svg>
      PO Box 3917 Marrowdene NSW 2279
    </li>
  </ul>

  <p class="abn">ABN: 41293087614</p>
</section>

<section class="card card--back" aria-label="Business card back">
  <div class="photo-area" role="img" aria-label="Photo of a snowboarder mid-jump above snowy mountain peaks under a deep blue sky"></div>
  <h2 class="wordmark">VANTREL CONSULTING</h2>
  <p class="services">Search &amp; Select<span class="sep">|</span>Career<span class="sep">|</span>Coaching<span class="sep">|</span>Leadership<span class="sep">|</span>Outplacement</p>
</section>

</body>
</html>
```